Green Logistics / Last Mile Delivery Firm needs cool one-page website

FYI - We do have a detailed brief in the uploaded files section below
COMPANY
We recently launched the company Brook Logistics which is a pioneer in urban green logistics and provides zero-emissions last mile delivery services (i.e. delivery of parcels with delivery vans to the doorstep of households) for its logistics and retail clients.
We take on urban parcel delivery for our clients with a 100% electric commercial vehicles fleet, fair and sustainable working conditions for our employees and an unparalleled professional and customer-focused mindset.
WEBSITE
In the detailed brief, we have provided examples to emulate. We need the design + coding of the website. Website needs to be friendly/optimized for and should open swiftly on both Android & iOS.
In general, the website should convey
- green mission of the company
- sustainability (good working conditions, focus on employees)
- customer orientation
- professionalism
DESIGN
In the detailed brief, we have provided designs to emulate.
Color design: we do have a logo which features 2 green colors (one lighter and one darker color tone). However, the colors on the website do not necessarily need to follow these 2 colors exactly as we are able to switch the logo colors.
Imagery: should reflect maybe 50% green/leaf/tree , 25% customer and employee orientation, and 25% logistics (here it's important that it is the last mile delivery, i.e. delivery with delivery vans to the doorstep of households)
Coding

```html
<!DOCTYPE html>
<html lang="en">
<head>
<meta charset="utf-8">
<title>Brook Logistics – Sustainable Last Mile</title>
<link href="https://fonts.googleapis.com/css2?family=Roboto:wght@300;400;500;700&display=swap" rel="stylesheet">
<style>
:root{
  --green:#6cb52d;
  --green-dark:#3f7d1c;
  --green-deep:#1f4a12;
  --ink:#2b2b2b;
  --text:#666;
  --muted:#999;
  --line:#e4e4e4;
  --paper:#ffffff;
  --soft:#f6f7f5;
  --footer:#1c2a16;
}
*{box-sizing:border-box;margin:0;padding:0}
html,body{width:1200px;height:4228px;overflow:hidden}
body{font-family:'Roboto',Arial,sans-serif;color:var(--text);background:var(--paper);font-size:12px;line-height:1.6}
.wrap{width:1200px;height:4228px;position:relative;overflow:hidden}
section,header{position:relative;width:1200px}
h2.title{font-size:30px;font-weight:700;color:var(--ink);text-align:center}
.bar{width:40px;height:3px;background:var(--green);margin:10px auto 0}
.btn{display:inline-block;background:var(--green);color:#fff;font-size:12px;font-weight:500;padding:8px 26px;border-radius:3px}
.btn.ghost{background:#fff;color:var(--green);border:1px solid var(--green)}
.foliage{position:absolute;background:radial-gradient(circle,rgba(108,181,45,.35) 0%,rgba(108,181,45,0) 70%)}

/* top bar */
.topbar{height:32px;background:var(--soft);border-bottom:1px solid var(--line);display:flex;align-items:center;justify-content:space-between;padding:0 112px;font-size:11px;color:var(--muted)}
.topbar .contacts span{margin-right:22px}
.topbar .langs span{display:inline-block;width:18px;height:11px;margin-left:8px;background:#ccc;border-radius:1px}

/* nav */
.nav{height:64px;display:flex;align-items:center;justify-content:space-between;padding:0 112px;background:#fff}
.brand{display:flex;align-items:center;gap:10px;font-size:17px;font-weight:700;color:var(--green-dark)}
.brand i{width:26px;height:26px;border-radius:50%;background:var(--green);display:block}
.menu{display:flex;gap:6px;font-size:12px;font-weight:500;color:var(--ink)}
.menu a{padding:8px 14px;border-radius:3px;color:inherit;text-decoration:none}
.menu a.on{background:var(--green);color:#fff}

/* hero */
.hero{height:564px;background:linear-gradient(180deg,#9fb6b4 0%,#b9c6b7 35%,#55703b 60%,#2f4a1d 100%);text-align:center;color:#fff}
.hero h1{position:absolute;top:150px;width:100%;font-size:38px;font-weight:700;text-shadow:0 2px 6px rgba(0,0,0,.35)}
.hero .sub{position:absolute;top:205px;width:100%;font-size:13px;letter-spacing:2px;font-weight:500}
.hero .btn{position:absolute;top:245px;left:540px;width:120px;text-align:center}
.hero .arrow{position:absolute;top:250px;width:30px;height:30px;border-radius:50%;background:rgba(255,255,255,.35)}
.hero .dots{position:absolute;top:524px;width:100%;display:flex;justify-content:center;gap:8px}
.hero .dots i{width:8px;height:8px;border-radius:50%;background:rgba(255,255,255,.55)}
.hero .dots i.on{background:#fff}

/* about */
.about{height:420px;padding-top:36px}
.about .cols{display:flex;gap:30px;padding:0 112px;margin-top:36px}
.about .col{flex:1;padding:26px 24px}
.about .col.card{background:#fff;box-shadow:0 6px 24px rgba(0,0,0,.12);margin-top:-14px}
.about .col h3{font-size:15px;color:var(--ink);margin:10px 0 10px;font-weight:700}
.icon{width:30px;height:30px}

/* is */
.is{height:460px;padding-top:40px}
.compare{position:absolute;top:104px;left:0;width:1200px;height:304px}
.ph{position:absolute}
.compare .train{left:0;top:0;width:288px;height:304px;background:linear-gradient(160deg,#c9a35a,#7d5a2e 55%,#44331f)}
.compare .woman{left:912px;top:0;width:288px;height:304px;background:linear-gradient(160deg,#e9e4dc,#b79d80 60%,#6b5a48)}
.box{position:absolute;top:24px;height:256px;padding:26px 30px}
.box h3{font-size:16px;font-weight:500;margin-bottom:18px}
.box li{list-style:none;font-size:11px;padding:7px 0;border-bottom:1px solid rgba(0,0,0,.08);text-align:right}
.box.plain{left:288px;width:312px;background:#fff;box-shadow:0 4px 20px rgba(0,0,0,.1);color:var(--ink)}
.box.green{left:600px;width:312px;top:8px;height:288px;background:var(--green);color:#fff}
.box.green h3{font-weight:700}
.box.green li{text-align:left;border-color:rgba(255,255,255,.25)}

/* services */
.services{height:460px;padding-top:48px}
.services .lead{width:760px;margin:18px auto 0;text-align:center;font-size:11px}
.cards{display:flex;gap:18px;padding:0 224px;margin-top:34px}
.cards .c{flex:1;text-align:center}
.cards .img{height:76px;margin-bottom:12px}
.cards h4{font-size:12px;color:var(--green-dark);font-weight:700}
.cards p{font-size:10px;margin-top:6px}

/* get in touch */
.touch{height:180px;background:linear-gradient(90deg,#1f4a12,#3a6b22 50%,#25511a);display:flex;align-items:center;justify-content:space-between;padding:0 224px;color:#fff}
.touch h3{font-size:20px;font-weight:700}
.touch p{font-size:10px;opacity:.85;width:520px;margin-top:6px}

/* careers */
.careers{height:1070px;padding-top:44px}
.careers .intro{position:absolute;top:120px;left:320px;width:680px;display:flex;gap:36px}
.careers .courier{width:244px;height:320px;background:linear-gradient(160deg,#d8d8d8,#8a3030 55%,#3a1f1f)}
.careers .intro p{font-size:11px;margin-bottom:12px}
.careers .call{position:absolute;top:468px;width:100%;text-align:center;font-size:17px;font-weight:700;color:var(--ink);line-height:1.5}
.job{position:absolute;top:548px;left:224px;width:752px;height:440px;border:1px solid var(--line);background:#fff}
.job .head{background:var(--soft);padding:10px 20px;font-size:11px;font-weight:700;color:var(--ink);border-bottom:1px solid var(--line)}
.job .body{display:flex;gap:30px;padding:18px 20px}
.job .body > div{flex:1}
.job h5{font-size:11px;color:var(--ink);margin:8px 0 6px}
.job li{list-style:none;font-size:10px;padding:4px 0 4px 16px;position:relative}
.job li:before{content:"";position:absolute;left:0;top:8px;width:8px;height:8px;border-radius:2px;border:1px solid var(--green)}
.offer{position:absolute;top:1004px;left:224px;width:752px;display:flex;justify-content:space-between;align-items:center}
.offer p{font-size:11px;color:var(--ink);width:320px}
.offer p b{color:var(--green)}
.offer .btns{display:flex;gap:14px}

/* map */
.map{height:230px}
.map .area{position:absolute;left:224px;top:8px;width:752px;height:212px;background:linear-gradient(135deg,#e8ecdf,#d9e2cc 50%,#ecefe6);border:1px solid var(--line)}

/* contact */
.contact{height:700px;background:linear-gradient(180deg,#ffffff 0%,#cfe3b4 12%,#4f8a27 55%,#24501a 100%)}
.contact h2{position:absolute;top:250px;width:100%}
.contact .bar{position:absolute;top:290px;left:580px;margin:0}
.panel{position:absolute;top:320px;left:224px;width:752px;height:320px;background:rgba(255,255,255,.92);padding:28px 30px;display:flex;gap:36px}
.info{width:270px}
.info .row{display:flex;gap:12px;margin-bottom:22px}
.info .dot{width:30px;height:30px;border-radius:50%;background:var(--green);flex:none;display:flex;align-items:center;justify-content:center}
.info b{display:block;font-size:11px;color:var(--ink)}
.info span{font-size:10px}
.form{flex:1}
.form .q{font-size:13px;font-weight:700;color:var(--ink);text-align:center}
.form .qs{font-size:10px;text-align:center;margin:4px 0 14px}
.form .two{display:flex;gap:12px}
.field{flex:1;height:30px;border:1px solid var(--line);background:#fff;font-size:10px;color:var(--muted);padding:7px 10px;margin-bottom:10px}
.field.area{height:96px}
.form .btn{display:block;width:140px;text-align:center;margin:4px auto 0}

/* footer */
.footer{height:48px;background:var(--footer);color:#aaa;font-size:10px;display:flex;align-items:center;justify-content:space-between;padding:0 112px}
.footer .soc{display:flex;gap:8px}
.footer .soc i{width:22px;height:22px;border-radius:50%;border:1px solid #667;display:block}
</style>
</head>
<body>
<div class="wrap">

<div class="topbar">
  <div class="contacts"><span>hello@brooklogistics.com</span><span>(555) 014-2290</span></div>
  <div class="langs"><span></span><span></span></div>
</div>

<header class="nav">
  <div class="brand"><i></i>Brook Logistics</div>
  <nav class="menu"><a class="on">HOME</a><a>ABOUT US</a><a>SERVICES</a><a>CAREERS</a><a>CONTACT US</a></nav>
</header>

<section class="hero" role="img" aria-label="Delivery truck driving on a country road between green trees">
  <div class="arrow" style="left:200px"></div>
  <div class="arrow" style="right:200px"></div>
  <h1>Brook Logistics – Sustainable Last Mile</h1>
  <div class="sub">BECAUSE WE CARE ABOUT TREES</div>
  <span class="btn">Get Started</span>
  <div class="dots"><i></i><i class="on"></i><i></i><i></i><i></i></div>
</section>

<section class="about">
  <div class="foliage" role="img" aria-label="Faint leaf pattern decoration" style="right:-60px;top:40px;width:200px;height:200px"></div>
  <h2 class="title">About Us</h2><div class="bar"></div>
  <div class="cols">
    <div class="col">
      <svg class="icon" viewBox="0 0 30 30"><circle cx="11" cy="10" r="5" fill="none" stroke="#6cb52d" stroke-width="2"/><circle cx="21" cy="11" r="4" fill="none" stroke="#6cb52d" stroke-width="2"/><path d="M3 26c0-6 4-9 8-9s8 3 8 9M18 19c4 0 9 2 9 7" fill="none" stroke="#6cb52d" stroke-width="2"/></svg>
      <h3>Who we are</h3>
      <p>We are a young company founded to make urban parcel delivery clean, quiet and fair. Our electric vans bring parcels to the doorstep of households for logistics and retail clients, with zero local emissions and a team that cares about each customer and every street we drive through.</p>
    </div>
    <div class="col card">
      <svg class="icon" viewBox="0 0 30 30"><circle cx="15" cy="15" r="12" fill="none" stroke="#6cb52d" stroke-width="2"/><circle cx="15" cy="15" r="6" fill="none" stroke="#6cb52d" stroke-width="2"/><circle cx="15" cy="15" r="2" fill="#6cb52d"/></svg>
      <h3>Our Mission</h3>
      <p>Our mission is to lead the green change of the last mile. We deliver with a fully electric fleet and plan every route for the shortest distance and lowest energy use.</p>
      <p style="margin-top:10px">We aim to show that clean delivery can also be reliable, fast and professional, so that cities breathe easier while parcels still arrive right on time.</p>
    </div>
    <div class="col">
      <svg class="icon" viewBox="0 0 30 30"><circle cx="15" cy="15" r="11" fill="none" stroke="#6cb52d" stroke-width="2"/><path d="M10 15l4 4 7-8" fill="none" stroke="#6cb52d" stroke-width="2"/></svg>
      <h3>Our values</h3>
      <p>We value fair pay, safe work and real respect for the people who drive our vans. Good working conditions make happy drivers, and happy drivers make happy customers. Honesty, care for nature and a clear focus on service guide all that we do each day.</p>
    </div>
  </div>
</section>

<section class="is">
  <h2 class="title">Brook Logistics is...</h2>
  <div class="compare">
    <div class="ph train" role="img" aria-label="Freight train at a station"></div>
    <div class="box plain">
      <h3>An Ordinary Parcel Delivery Firm</h3>
      <ul><li>Polluting diesel vans</li><li>Missed and late drops</li><li>Poor driver conditions</li><li>Little care for customers</li><li>Old-fashioned route planning</li></ul>
    </div>
    <div class="box green">
      <h3>A pioneering Green Last Mile</h3>
      <ul><li>100% electric delivery fleet</li><li>Fair and safe jobs for drivers</li><li>Customer focus at every door</li><li>Smart and efficient routes</li><li>Zero local emissions in cities</li></ul>
    </div>
    <div class="ph woman" role="img" aria-label="Customer receiving a parcel at her door"></div>
  </div>
  <div class="foliage" role="img" aria-label="Falling leaf decoration" style="left:10px;top:400px;width:90px;height:90px"></div>
</section>

<section class="services">
  <h2 class="title">Our Services</h2><div class="bar"></div>
  <p class="lead">We take on urban parcel delivery for our clients with electric vans, trained drivers and a service mindset. From the depot to the doorstep, each parcel is handled with care, tracked in real time and delivered with a friendly face.</p>
  <div class="cards">
    <div class="c"><div class="img" role="img" aria-label="Electric delivery van" style="background:linear-gradient(135deg,#cfd8c4,#7a9a5a)"></div><h4>Zero-emission delivery</h4><p>Clean electric vans for every city route.</p></div>
    <div class="c"><div class="img" role="img" aria-label="Driver handing over a parcel" style="background:linear-gradient(135deg,#e2d6c6,#9c7a58)"></div><h4>Highly trained delivery drivers</h4><p>Skilled staff who know each street well.</p></div>
    <div class="c"><div class="img" role="img" aria-label="Courier in red uniform with boxes" style="background:linear-gradient(135deg,#e6d3d0,#a4403a)"></div><h4>Professional all-around</h4><p>Reliable planning, tracking and handover.</p></div>
    <div class="c"><div class="img" role="img" aria-label="Smiling customer with parcel" style="background:linear-gradient(135deg,#dfe6ea,#7e95a4)"></div><h4>Unparalleled customer focus</h4><p>Friendly service at every single door.</p></div>
  </div>
</section>

<section class="touch" role="img" aria-label="Green forest band">
  <div><h3>Get in touch with Brook Logistics</h3><p>Are you looking for a clean and reliable last mile partner? Talk to our team today and learn how we can bring your parcels home.</p></div>
  <span class="btn">Contact Us</span>
</section>

<section class="careers">
  <div class="foliage" role="img" aria-label="Green plant decoration" style="right:-60px;top:20px;width:220px;height:220px"></div>
  <div class="foliage" role="img" aria-label="Green plant decoration" style="left:-60px;top:0;width:180px;height:180px"></div>
  <h2 class="title">Careers</h2><div class="bar"></div>
  <div class="intro">
    <div class="courier" role="img" aria-label="Courier carrying a red delivery bag"></div>
    <div style="flex:1;padding-top:20px">
      <p>At Brook Logistics, people come first. We are building a team of drivers who enjoy the road, care about the city and want a job with real purpose. We offer fair pay, steady hours and modern electric vans.</p>
      <p>Our drivers are the face of the company. They meet our customers every day, so we invest in training, safety and a good team spirit. Every route is planned to keep the work day calm and balanced.</p>
      <p>If you want to grow with a young company that takes its green mission seriously, we would love to hear from you and tell you more about our open roles.</p>
    </div>
  </div>
  <div class="call">If you are excited about joining our Brook Logistics family,<br>please check out our open positions.</div>
  <div class="job">
    <div class="head">Full-time driver / parcel delivery (m/f/d) in the city</div>
    <div class="body">
      <div>
        <p style="font-size:10px">We are looking for reliable drivers to join our growing city team as soon as possible.</p>
        <h5>Your tasks as a delivery driver</h5>
        <ul><li>Delivery of packages to our customers</li><li>Loading and checking the van each morning</li><li>Following the planned route on time</li><li>Handing over parcels with a friendly word</li><li>Reporting any issues to the depot team</li><li>Keeping the electric van clean and safe</li></ul>
        <h5>Required knowledge and skills</h5>
        <ul><li>Valid driving licence for small vans</li><li>Reliability and a careful driving style</li><li>Good basic language skills</li><li>Friendly manner with customers</li><li>Some delivery experience is a plus</li></ul>
      </div>
      <div>
        <h5>What you can expect from Brook Logistics</h5>
        <ul><li>A fair and open team culture</li><li>Permanent contract with steady pay</li><li>Modern and quiet electric vans</li><li>Clear shift plans and calm routes</li><li>Paid training from day one</li><li>Safety gear and work clothing</li><li>Bonus for great customer feedback</li><li>Room to grow into team lead roles</li><li>Regular team events and meals</li><li>Support from a friendly depot team</li></ul>
      </div>
    </div>
  </div>
  <div class="offer">
    <p>We offer a secure and varied job in a rapidly growing company with opportunities for advancement. <b>INTERESTED?</b></p>
    <div class="btns"><span class="btn">Send us an Email</span><span class="btn ghost">Give us a Call</span></div>
  </div>
</section>

<section class="map">
  <div class="area" role="img" aria-label="Map showing the company location"></div>
</section>

<section class="contact" role="img" aria-label="Green grass background with sunlight">
  <h2 class="title">Contact Us</h2><div class="bar"></div>
  <div class="panel">
    <div class="info">
      <div class="row"><div class="dot"><svg width="12" height="14" viewBox="0 0 12 14"><path d="M6 13S1 8 1 5a5 5 0 0110 0c0 3-5 8-5 8z" fill="#fff"/></svg></div><div><b>LOCATION</b><span>Harbor Row 12, Millford</span></div></div>
      <div class="row"><div class="dot"><svg width="14" height="10" viewBox="0 0 14 10"><rect x="1" y="1" width="12" height="8" fill="none" stroke="#fff"/><path d="M1 1l6 5 6-5" fill="none" stroke="#fff"/></svg></div><div><b>EMAIL ADDRESS</b><span>hello@brooklogistics.com</span></div></div>
      <div class="row"><div class="dot"><svg width="12" height="12" viewBox="0 0 12 12"><path d="M2 1l3 1 1 3-2 1c1 2 2 3 4 4l1-2 3 1v3c-6 0-10-4-11-11z" fill="#fff"/></svg></div><div><b>CALL US</b><span>(555) 014-2290</span></div></div>
    </div>
    <div class="form">
      <div class="q">We'd love to hear from you!</div>
      <div class="qs">Send us a message and our team will reply within one working day.</div>
      <div class="two"><div class="field">Name</div><div class="field">Email</div></div>
      <div class="field">Subject</div>
      <div class="field area">Message</div>
      <span class="btn">Send Message</span>
    </div>
  </div>
</section>

<footer class="footer">
  <div>Legal Notice &nbsp;&nbsp; Privacy Policy</div>
  <div>Copyright © Brook Logistics 2024. All rights reserved.</div>
  <div class="soc"><i></i><i></i><i></i><i></i></div>
</footer>

</div>
</body>
</html>
```